Non profit organization looking for new flyers as "leaflets"

Hi, we are looking for new flyers in form "leaflets in German :-)" i've attached our old flyer, we have new logo and thats why we need new and better design smt ... "New: I've so attached the text Regarding the old cards with minor changes "

Industry/Entity Type

Non Profit

Font styles to use
Sans Serif

```html
<!DOCTYPE html>
<html lang="de">
<head>
<meta charset="utf-8">
<title>Lumora – Ambulante Erziehungshilfe Leaflet</title>
<link href="https://fonts.googleapis.com/css2?family=Open+Sans:wght@400;600;700;800&display=swap" rel="stylesheet">
<style>
:root{
  --green:#7ab51d;
  --green-dark:#5e9412;
  --ink:#3e4347;
  --ink-dark:#2c3033;
  --blue:#2d5f8f;
  --grey-light:#e9eaeb;
  --grey-mid:#c9ccce;
  --paper:#ffffff;
  --bg:#f1f2f3;
}
*{box-sizing:border-box;margin:0;padding:0}
html,body{width:900px;height:1200px;overflow:hidden;background:var(--bg);font-family:"Open Sans",Arial,sans-serif;color:var(--ink)}
.spread{position:absolute;left:30px;width:840px;height:555px;background:var(--paper);display:flex;box-shadow:0 2px 6px rgba(0,0,0,.15)}
.spread.outside{top:30px}
.spread.inside{top:615px}
.panel{position:relative;width:280px;height:100%;overflow:hidden;border-right:1px solid #e2e3e4}
.panel:last-child{border-right:none}
.photo{position:absolute;display:block}
.band{position:absolute;left:0;height:22px;padding:0 14px;display:flex;align-items:center;color:#fff;font-weight:700;font-size:10.5px;letter-spacing:.5px;text-transform:uppercase}
.band.dark{background:var(--ink-dark);border-left:5px solid var(--green)}
.band.green{background:var(--green)}
.checklist{position:absolute;left:14px;right:14px;list-style:none;font-size:7.4px;line-height:1.45}
.checklist li{position:relative;padding-left:11px;margin-bottom:2px}
.checklist li::before{content:"";position:absolute;left:0;top:3px;width:5px;height:5px;background:var(--green)}
.checklist.on-dark{color:#fff}
.brand{position:absolute;display:flex;align-items:center;gap:6px;font-weight:800;color:var(--ink-dark);letter-spacing:-.3px}
.brand .mark{background:var(--green);display:inline-block}
.web{position:absolute;font-size:7.5px;color:var(--ink)}
.top-grad{position:absolute;left:0;top:0;width:100%;height:32px;background:linear-gradient(#f7f7f7,#d7d9da)}
.headline-small{position:absolute;left:14px;top:10px;font-size:10px;font-weight:800;color:var(--ink-dark);letter-spacing:.4px}
.location-title{position:absolute;left:0;width:100%;text-align:center;color:var(--green);font-weight:700;font-size:15px}
.address{position:absolute;left:0;width:100%;text-align:center;font-size:7px;line-height:1.5;color:var(--ink)}
.title-main{position:absolute;right:16px;text-align:right;font-weight:800;color:var(--ink-dark);font-size:27px;letter-spacing:.5px;line-height:1}
.title-sub{position:absolute;right:16px;text-align:right;font-weight:700;color:var(--green);font-size:13px;letter-spacing:1.5px}
.info-box{position:absolute;left:0;top:138px;width:280px;height:190px;background:var(--blue);color:#fff;padding:12px 16px;font-size:7.4px;line-height:1.5}
.law-list{list-style:none;margin-top:16px}
.law-list li{display:flex;align-items:baseline;font-weight:600;margin-bottom:3px}
.law-list .dots{flex:1;border-bottom:1px dotted rgba(255,255,255,.7);margin:0 4px}
.law-note{position:absolute;left:14px;top:338px;font-size:15.5px;font-weight:800;color:var(--green);letter-spacing:.3px}
.body-text{position:absolute;left:16px;right:16px;font-size:7.4px;line-height:1.5;color:var(--ink)}
</style>
</head>
<body>

<!-- Outside spread -->
<section class="spread outside">
  <div class="panel panel-goals">
    <div class="top-grad"></div>
    <p class="headline-small">WER STÄNDIG GLÜCKLICH</p>
    <div class="photo" role="img" aria-label="Stimmungsfoto im Kopfbereich" style="left:0;top:32px;width:280px;height:30px;background:linear-gradient(90deg,#dfe1e2,#f4f4f4)"></div>
    <div class="band dark" style="top:64px;width:150px">Unsere Ziele</div>
    <div style="position:absolute;left:0;top:90px;width:280px;height:128px;background:var(--green)"></div>
    <ul class="checklist on-dark" style="top:98px">
      <li>Stärkung der Erziehungskompetenz in der Familie</li>
      <li>Förderung der Entwicklung und Selbstständigkeit</li>
      <li>Sicherung des Kindeswohls im häuslichen Umfeld</li>
      <li>Klärung und Bewältigung familiärer Konflikte</li>
      <li>Aufbau tragfähiger Beziehungen zwischen Eltern und Kind</li>
      <li>Vermeidung stationärer Unterbringung</li>
      <li>Integration in Schule, Ausbildung und Beruf</li>
    </ul>
    <div class="brand" style="left:60px;top:236px;font-size:30px"><span class="mark" style="width:22px;height:22px"></span>Lumora</div>
    <div class="photo" role="img" aria-label="Foto eines Telefons auf dem Schreibtisch" style="left:0;top:300px;width:280px;height:255px;background:linear-gradient(160deg,#f2f2f2,#b9bcbe 60%,#6d7275)"></div>
  </div>

  <div class="panel panel-contact">
    <div class="photo" role="img" aria-label="Foto einer Mutter mit Kindern" style="left:0;top:0;width:280px;height:300px;background:linear-gradient(150deg,#c9a58b,#e6d3c2 45%,#9b7d69)"></div>
    <p class="location-title" style="top:308px">Location</p>
    <p class="address" style="top:332px">Musterstraße 12 · 10115 Berlin<br>Telefon 030 123 456 78<br>Telefax 030 123 456 79</p>
    <p class="address" style="top:378px">Büro Nord · Lindenweg 4<br>Telefon 030 987 654 32</p>
    <p class="address" style="top:412px">Beratung nach Vereinbarung<br>Mo–Fr 9:00–17:00 Uhr</p>
    <p class="web" style="left:0;width:100%;text-align:center;top:536px">www.lumora-hilfe.de</p>
  </div>

  <div class="panel panel-cover">
    <div class="brand" style="right:16px;top:14px;font-size:26px"><span class="mark" style="width:20px;height:20px"></span>Lumora</div>
    <div class="photo" role="img" aria-label="Foto einer Familie mit Kindern" style="left:0;top:58px;width:280px;height:230px;background:linear-gradient(135deg,#d6b59c,#f1e4d8 50%,#a88a74)"></div>
    <p class="title-main" style="top:398px">AMBULANTE</p>
    <p class="title-sub" style="top:428px">ERZIEHUNGSHILFE</p>
    <div style="position:absolute;left:0;bottom:0;width:280px;height:26px;background:var(--ink-dark);border-top:3px solid var(--green)"></div>
    <p class="web" style="right:16px;bottom:9px;color:#fff">www.lumora-hilfe.de</p>
  </div>
</section>

<!-- Inside spread -->
<section class="spread inside">
  <div class="panel panel-groups">
    <div class="brand" style="left:60px;top:14px;font-size:26px"><span class="mark" style="width:20px;height:20px"></span>Lumora</div>
    <div class="band dark" style="top:64px;width:170px">Unsere Zielgruppen</div>
    <ul class="checklist" style="top:94px">
      <li>Kinder und Jugendliche mit Entwicklungs- und Verhaltensauffälligkeiten</li>
      <li>Familien in belastenden Lebenslagen und Krisen</li>
      <li>Alleinerziehende Mütter und Väter</li>
      <li>Kinder und Jugendliche mit Migrationshintergrund</li>
      <li>Junge Volljährige auf dem Weg in die Selbstständigkeit</li>
    </ul>
    <div class="photo" role="img" aria-label="Foto spielender Kinder" style="left:0;top:205px;width:280px;height:240px;background:linear-gradient(150deg,#b8c8d4,#eef1f3 45%,#8c9aa5)"></div>
    <ul class="checklist" style="top:455px">
      <li>Familien mit Unterstützungsbedarf im Alltag</li>
      <li>Eltern mit psychischen oder gesundheitlichen Belastungen</li>
      <li>Pflege- und Adoptivfamilien</li>
    </ul>
    <p class="web" style="left:0;width:100%;text-align:center;top:536px">www.lumora-hilfe.de</p>
  </div>

  <div class="panel panel-offers">
    <div class="band green" style="top:64px;width:170px">Unsere Angebote</div>
    <ul class="checklist" style="top:94px">
      <li>Sozialpädagogische Familienhilfe</li>
      <li>Erziehungsbeistandschaft</li>
      <li>Einzelbetreuung</li>
      <li>Intensive sozialpädagogische Einzelbetreuung</li>
      <li>Soziale Gruppenarbeit</li>
      <li>Begleiteter Umgang</li>
      <li>Beratung in Trennungssituationen</li>
      <li>Elterntraining und Elterncafé</li>
    </ul>
    <div class="brand" style="left:70px;top:218px;font-size:28px"><span class="mark" style="width:20px;height:20px"></span>Lumora</div>
    <div class="photo" role="img" aria-label="Foto einer Mutter mit Kind" style="left:0;top:272px;width:280px;height:180px;background:linear-gradient(140deg,#d9c3b0,#f4ece4 50%,#b0937d)"></div>
    <ul class="checklist" style="top:462px">
      <li>Hilfeplanung gemeinsam mit dem Jugendamt</li>
      <li>Krisenintervention</li>
      <li>Netzwerkarbeit im Sozialraum</li>
    </ul>
  </div>

  <div class="panel panel-team">
    <div class="photo" role="img" aria-label="Foto einer lachenden Familie" style="left:0;top:0;width:280px;height:138px;background:linear-gradient(135deg,#e8d6c6,#f8f2ec 50%,#c2a58e)"></div>
    <div class="info-box">
      <p>Wir bieten flexible, ambulante Hilfen zur Erziehung für Kinder, Jugendliche und ihre Familien. Unser Angebot richtet sich nach dem individuellen Bedarf und orientiert sich an den Stärken jeder Familie.</p>
      <ul class="law-list">
        <li>Hilfe zur Erziehung<span class="dots"></span>§27</li>
        <li>Erziehungsberatung<span class="dots"></span>§28</li>
        <li>Soziale Gruppenarbeit<span class="dots"></span>§29</li>
        <li>Erziehungsbeistand<span class="dots"></span>§30</li>
        <li>Familienhilfe<span class="dots"></span>§31</li>
        <li>Einzelbetreuung<span class="dots"></span>§35</li>
      </ul>
    </div>
    <p class="law-note">(IN VERBINDUNG MIT §41)</p>
    <div class="band dark" style="top:372px;width:150px">Unser Team</div>
    <p class="body-text" style="top:400px">Unser Team besteht aus qualifizierten Fachkräften mit langjähriger Erfahrung in der Kinder- und Jugendhilfe. Durch regelmäßige Supervision und Fortbildung sichern wir die Qualität unserer Arbeit und begleiten Familien verlässlich.</p>
    <div class="photo" role="img" aria-label="Foto des Teams bei einer Besprechung" style="left:0;top:462px;width:280px;height:93px;background:linear-gradient(150deg,#c5c9cc,#eceeef 50%,#8f969b)"></div>
  </div>
</section>

</body>
</html>
```